Uprising SaaS company needs an attractive business card design

We're an uprising SaaS company who's attempting to attack the rigid car (insurance) claims management market in Europe.
We want to our mighty base order management system, listen to our clients to connect the smart ideas to build something even mightier.
We primarily focus on helping our customers manage their customers' claims/orders and get them resolved as smoothly as possible.
We'd like the business card design to express technical innovation and the fact that we connect smart ideas, as our company slogan indicates.
Contact Information for Business Card
Name, position, website, email, mobile, business address
Font styles to use
Colors
Designer to choose colors to be used in the design.
Look and feel
Each slider illustrates characteristics of the customer's brand and the style your logo design should communicate.

```html
<!DOCTYPE html>
<html lang="en">
<head>
<meta charset="utf-8">
<title>ostralyn business card</title>
<link rel="stylesheet" href="https://fonts.googleapis.com/css2?family=Montserrat:wght@400;500;600&display=swap">
<style>
  :root {
    --backdrop: #e9e7e4;
    --card-white: #ffffff;
    --card-navy: #0d0a2a;
    --ink: #1d1d1f;
    --grey: #7d7d80;
    --sky: #7ccbe0;
    --rule: #6f6f72;
  }
  * { box-sizing: border-box; margin: 0; padding: 0; }
  html, body {
    width: 1200px; height: 1000px; overflow: hidden;
    background: var(--backdrop);
    font-family: "Montserrat", sans-serif;
  }
  .sheet { position: relative; width: 1200px; height: 1000px; }
  .card {
    position: absolute; left: 220px; width: 760px; height: 434px;
    box-shadow: 0 6px 20px rgba(0,0,0,0.12);
  }
  .card-front { top: 50px; background: var(--card-white); }
  .card-back { top: 516px; background: var(--card-navy); }

  .wordmark {
    display: flex; align-items: center; gap: 14px;
    font-weight: 400; letter-spacing: 2px; white-space: nowrap;
  }
  .wordmark-dot { border-radius: 50%; flex: none; }

  .card-front .wordmark {
    position: absolute; left: 56px; top: 188px;
    font-size: 48px; color: var(--grey);
  }
  .card-front .wordmark-dot { width: 14px; height: 14px; background: var(--sky); }

  .divider {
    position: absolute; left: 418px; top: 52px; width: 3px; height: 330px;
    background: var(--rule);
  }
  .contact {
    position: absolute; left: 452px; top: 58px; color: var(--ink);
    font-size: 19px; font-weight: 500; line-height: 1.3; white-space: nowrap;
  }
  .contact-name { color: var(--sky); font-weight: 600; font-size: 20px; }
  .contact-role { color: var(--grey); font-weight: 600; margin-bottom: 18px; }
  .contact-address { margin-bottom: 16px; }
  .contact-line { display: flex; align-items: center; gap: 16px; margin-bottom: 12px; }
  .contact-line svg { width: 20px; height: 20px; flex: none; }

  .card-back .wordmark {
    position: absolute; left: 0; right: 0; top: 160px; justify-content: center;
    font-size: 92px; color: var(--sky);
  }
  .card-back .wordmark-dot { width: 22px; height: 22px; background: var(--sky); }
</style>
</head>
<body>
<main class="sheet">
  <section class="card card-front" aria-label="Business card front">
    <div class="wordmark"><span class="wordmark-dot"></span><span>ostralyn</span></div>
    <div class="divider"></div>
    <div class="contact">
      <p class="contact-name">Jonas Weber</p>
      <p class="contact-role">CEO</p>
      <p class="contact-address">ostralyn GmbH<br>Lindenweg 14b<br>10115 Berlin - Germany</p>
      <p class="contact-line">
        <svg viewBox="0 0 20 20" aria-hidden="true"><path d="M5 2.5l3 3-1.8 2a10 10 0 0 0 6.3 6.3l2-1.8 3 3-2 2.5C9 17 3 11 2.5 4.5z" fill="none" stroke="#7ccbe0" stroke-width="1.6" stroke-linejoin="round"/></svg>
        <span>(111) 555-0182</span>
      </p>
      <p class="contact-line">
        <svg viewBox="0 0 20 20" aria-hidden="true"><rect x="2" y="4.5" width="16" height="11" fill="#7ccbe0"/><path d="M2 4.5l8 6 8-6" fill="none" stroke="#fff" stroke-width="1.4"/></svg>
        <span>(111) 555-0182</span>
      </p>
      <p class="contact-line">
        <svg viewBox="0 0 20 20" aria-hidden="true"><g fill="none" stroke="#7ccbe0" stroke-width="1.4"><circle cx="10" cy="10" r="8"/><ellipse cx="10" cy="10" rx="3.5" ry="8"/><path d="M2 10h16M3.5 6h13M3.5 14h13"/></g></svg>
        <span>https ostralyn.com</span>
      </p>
    </div>
  </section>

  <section class="card card-back" aria-label="Business card back">
    <div class="wordmark"><span class="wordmark-dot"></span><span>ostralyn</span></div>
  </section>
</main>
</body>
</html>
```